Marova Hand Wash

Design hand washes. Total 12 variants to be designed.

Variants name are:

1) MILK &OLIVE
2) Shea Butter
3) Hidden Glow
4) Cream and Peach
5) Milk and Honey
6) Amber Riddle
7) Bakhour
8) Musk
9) White Oud
10) Black Oud
11) Rose Oud
12) Oud & Sandalwood

Labels can be on transparent sticker or background colors. All variants will be differentiated by fragrances and color. Bottle will be transparent. Pumps used for dispensing will be in Black or Transparent Color.

Designers can initially present designs of 4-5 variants initially. Later based on feedback, they can work out on more.

Bottle is 400ml and shape is rectangle. Ignore the size on bottle picture. Bottle keyline is attached.

Target Market(s)

B+, B, C+

Requirements
Must have
• Some relation to the variant names

```html
<!DOCTYPE html>
<html lang="en">
<head>
<meta charset="utf-8">
<title>Marova Hand Wash Labels</title>
<link rel="stylesheet" href="https://fonts.googleapis.com/css2?family=Kaushan+Script&family=Quicksand:wght@500;600;700&family=Playfair+Display:ital@1&display=swap">
<style>
  :root {
    --canvas: #ffffff;
    --brand-purple: #7a5cb8;
    --brand-dot: #8a3a4a;
    --rule-green: #7cc242;
    --olive-green: #45a82a;
    --olive-bg-top: #e9f7c4;
    --olive-bg-bottom: #f4fae6;
    --shea-brown: #7a4a1c;
    --shea-bg: #f6f6f6;
    --bakhour-brown: #7a4514;
    --bakhour-bg-top: #fbf3ea;
    --bakhour-bg-bottom: #f3e0c8;
    --ink: #2a2a2a;
    --pill-orange: #f07a1c;
    --pill-orange-dark: #d9581a;
    --pill-brown: #8a4a26;
    --pill-gold: #e8a526;
  }
  * { box-sizing: border-box; margin: 0; padding: 0; }
  html, body { width: 1200px; height: 732px; overflow: hidden; background: var(--canvas); }
  .canvas {
    position: relative; width: 1200px; height: 732px;
    display: flex; justify-content: center; align-items: center; gap: 85px;
  }
  .label {
    position: relative; width: 300px; height: 560px; border-radius: 26px;
    overflow: hidden; box-shadow: 0 2px 10px rgba(0,0,0,0.08);
    font-family: "Quicksand", sans-serif;
  }
  .label--olive { background: linear-gradient(180deg, var(--olive-bg-top), var(--olive-bg-bottom)); }
  .label--shea { background: var(--shea-bg); }
  .label--bakhour { background: linear-gradient(180deg, var(--bakhour-bg-top), var(--bakhour-bg-bottom)); }

  .brand {
    position: absolute; top: 46px; left: 0; right: 0;
    display: flex; justify-content: center; align-items: center; gap: 8px;
  }
  .brand__name {
    font-family: "Quicksand", sans-serif; font-weight: 700; font-size: 44px;
    color: var(--brand-purple); letter-spacing: 0.5px;
  }
  .brand__dot { width: 12px; height: 12px; border-radius: 50%; background: var(--brand-dot); }

  .pure {
    position: absolute; top: 148px; left: 0; right: 0;
    display: flex; justify-content: center; align-items: center; gap: 8px;
    font-family: "Playfair Display", serif; font-style: italic; font-size: 13px; color: var(--olive-green);
  }
  .pure::before, .pure::after { content: ""; width: 28px; height: 1px; background: var(--rule-green); }

  .title {
    position: absolute; left: 0; right: 0; text-align: center;
    font-family: "Kaushan Script", cursive; line-height: 0.9;
  }
  .title--olive { top: 168px; color: var(--olive-green); font-size: 54px; }
  .title--olive .title__first { color: #ffffff; text-shadow: 0 0 1px #9ab88a, 0 1px 2px rgba(0,0,0,0.25); }
  .title--shea { top: 168px; color: var(--shea-brown); font-size: 56px; }
  .title--bakhour { top: 196px; color: var(--bakhour-brown); font-size: 56px; }

  .kind {
    position: absolute; right: 34px;
    font-family: "Quicksand", sans-serif; font-weight: 600; font-size: 13px; color: var(--ink);
  }
  .kind--olive { top: 290px; }
  .kind--shea { top: 290px; }
  .kind--bakhour { top: 262px; }

  .photo { position: absolute; left: 0; right: 0; bottom: 0; }
  .photo--olive {
    top: 322px;
    background: radial-gradient(ellipse at 50% 40%, #8a8a3a 0%, #b9b04a 25%, #e8d98a 45%, rgba(255,255,255,0.9) 70%, #ffffff 100%);
  }
  .photo--shea {
    top: 310px;
    background: radial-gradient(ellipse at 50% 50%, #f1eadb 0%, #ece3cf 35%, #e7e7e7 65%, #f6f6f6 100%);
  }
  .photo--bakhour {
    top: 290px;
    background:
      linear-gradient(180deg, rgba(0,0,0,0) 70%, #4a2e18 82%, #2e1c0e 100%),
      radial-gradient(ellipse at 50% 45%, #e1b83a 0%, #c38e1e 28%, #e9d2b0 55%, rgba(243,224,200,0) 80%);
  }

  .volume {
    position: absolute; bottom: 22px; left: 50%; transform: translateX(-50%);
    padding: 3px 12px; border-radius: 12px;
    font-family: "Quicksand", sans-serif; font-weight: 700; font-size: 13px; color: #ffffff;
  }
  .volume--olive { background: linear-gradient(180deg, var(--pill-orange), var(--pill-orange-dark)); }
  .volume--shea { background: var(--pill-brown); }
  .volume--bakhour { background: linear-gradient(180deg, var(--pill-gold), var(--pill-orange)); }
</style>
</head>
<body>
<main class="canvas">

  <section class="label label--olive">
    <div class="brand"><span class="brand__name">Marova</span><span class="brand__dot"></span></div>
    <div class="pure">Pure</div>
    <h2 class="title title--olive"><span class="title__first">Milk</span><br>&amp; Olive</h2>
    <div class="kind kind--olive">HAND WASH</div>
    <div class="photo photo--olive" role="img" aria-label="Green and purple olives with splashing olive oil and milk"></div>
    <div class="volume volume--olive">400ML</div>
  </section>

  <section class="label label--shea">
    <div class="brand"><span class="brand__name">Marova</span><span class="brand__dot"></span></div>
    <div class="pure">Pure</div>
    <h2 class="title title--shea">Shea<br>Butter</h2>
    <div class="kind kind--shea">HAND WASH</div>
    <div class="photo photo--shea" role="img" aria-label="Whipped shea butter in a glass bowl topped with shea nuts and leaves, over a milk splash"></div>
    <div class="volume volume--shea">400ML</div>
  </section>

  <section class="label label--bakhour">
    <div class="brand"><span class="brand__name">Marova</span><span class="brand__dot"></span></div>
    <div class="pure">Pure</div>
    <h2 class="title title--bakhour">Bakhour</h2>
    <div class="kind kind--bakhour">HAND WASH</div>
    <div class="photo photo--bakhour" role="img" aria-label="Ornate golden incense burner with rising smoke on a bed of oud wood chips"></div>
    <div class="volume volume--bakhour">400ML</div>
  </section>

</main>
</body>
</html>
```